Haverill’s

I would like a high class looking card with my logo and contact details (as per uploaded) Elegant, professional and highest quality feel

The following text included …..
“All commercial and residential painting work, large or small. Highest quality finishes and service.”

Industry/Entity Type

Painting

Contact Information for Business Card

Name, phone number, address, email address, company logo

Requirements
Must have
• Double sided

```html
<!DOCTYPE html>
<html lang="en">
<head>
<meta charset="utf-8">
<title>Haverill’s – Business Card</title>
<link href="https://fonts.googleapis.com/css2?family=Open+Sans:wght@400;600;700&display=swap" rel="stylesheet">
<style>
  :root {
    --stage: #2b2b2e;
    --card-dark: #1f1e23;
    --gold: #b9843f;
    --gold-light: #c8944d;
    --gold-deep: #a8743a;
    --ink-light: #ffffff;
    --rule: #7a7a80;
  }
  * { box-sizing: border-box; margin: 0; padding: 0; }
  html, body { width: 1200px; height: 780px; overflow: hidden; }
  body {
    background: var(--stage);
    font-family: "Open Sans", Arial, sans-serif;
    position: relative;
  }
  .card {
    position: absolute;
    top: 235px;
    width: 540px;
    height: 310px;
    border-radius: 4px;
    overflow: hidden;
  }
  .card-front { left: 45px; background: var(--card-dark); }
  .card-back { left: 615px; }

  /* brand name */
  .brand {
    position: absolute;
    display: flex;
    align-items: center;
    gap: 12px;
  }
  .brand-name {
    font-weight: 600;
    letter-spacing: 1px;
  }
  .brand-dot {
    border-radius: 50%;
    flex: none;
  }
  .card-front .brand { top: 42px; right: 42px; }
  .card-front .brand-name { font-size: 32px; color: var(--gold); }
  .card-front .brand-dot { width: 34px; height: 34px; border: 2px solid var(--gold); }

  /* identity */
  .person {
    position: absolute;
    top: 128px;
    left: 40px;
    width: 210px;
    text-align: right;
  }
  .person-name { font-size: 25px; font-weight: 700; color: var(--gold); line-height: 1.2; }
  .person-role { font-size: 15px; color: var(--ink-light); margin-top: 4px; }

  .divider {
    position: absolute;
    left: 268px;
    top: 120px;
    width: 1px;
    height: 110px;
    background: var(--rule);
  }

  .contact {
    position: absolute;
    left: 286px;
    top: 118px;
    color: var(--ink-light);
    font-size: 13.5px;
    line-height: 1.45;
    list-style: none;
  }
  .contact-address { margin-bottom: 4px; }
  .contact-item { display: flex; align-items: center; gap: 8px; }
  .contact-item svg { width: 12px; height: 12px; flex: none; }

  .service-band {
    position: absolute;
    left: 0; right: 0; bottom: 0;
    height: 64px;
    background: var(--gold);
    color: var(--ink-light);
    font-size: 14px;
    line-height: 1.4;
    padding: 12px 40px;
  }

  /* back */
  .monogram-field {
    position: absolute;
    inset: 0;
    background: linear-gradient(120deg, var(--gold-deep) 0%, var(--gold) 55%, var(--gold-light) 100%);
  }
  .card-back .brand { top: 50%; left: 50%; transform: translate(-50%, -50%); }
  .card-back .brand-name { font-size: 40px; color: var(--ink-light); }
  .card-back .brand-dot { width: 42px; height: 42px; border: 2px solid var(--ink-light); }
</style>
</head>
<body>

<section class="card card-front">
  <div class="brand">
    <span class="brand-name">Haverill’s</span>
    <span class="brand-dot"></span>
  </div>

  <div class="person">
    <p class="person-name">Owen Haverill</p>
    <p class="person-role">Owner</p>
  </div>

  <div class="divider"></div>

  <ul class="contact">
    <li class="contact-address">42 Kowhai Terrace,<br>Waimarie, 3517</li>
    <li class="contact-item">
      <svg viewBox="0 0 24 24" aria-hidden="true"><path fill="#b9843f" d="M6.6 10.8a15 15 0 0 0 6.6 6.6l2.2-2.2a1 1 0 0 1 1-.25 11.4 11.4 0 0 0 3.6.57 1 1 0 0 1 1 1V20a1 1 0 0 1-1 1A17 17 0 0 1 3 4a1 1 0 0 1 1-1h3.5a1 1 0 0 1 1 1c0 1.25.2 2.45.57 3.6a1 1 0 0 1-.25 1z"/></svg>
      021 555 0147
    </li>
    <li class="contact-item">
      <svg viewBox="0 0 24 24" aria-hidden="true"><circle cx="12" cy="12" r="10" fill="none" stroke="#b9843f" stroke-width="2.4"/><path d="M2 12h20M12 2c3 3 3 17 0 20M12 2c-3 3-3 17 0 20" fill="none" stroke="#b9843f" stroke-width="2"/></svg>
      www.haverills.co.nz
    </li>
    <li class="contact-item">
      <svg viewBox="0 0 24 24" aria-hidden="true"><rect x="2" y="5" width="20" height="14" rx="2" fill="#b9843f"/><path d="M3 6l9 7 9-7" fill="none" stroke="#1f1e23" stroke-width="2"/></svg>
      owen@haverills.co.nz
    </li>
  </ul>

  <p class="service-band">All commercial and residential painting work,<br>large or small. Highest quality finishes and service</p>
</section>

<section class="card card-back">
  <div class="monogram-field" role="img" aria-label="Repeating embossed monogram pattern in gold tones"></div>
  <div class="brand">
    <span class="brand-name">Haverill’s</span>
    <span class="brand-dot"></span>
  </div>
</section>

</body>
</html>
```